Kip's Pharmacy Business Card Design Project

I need a business card designed for my pharmacy Kip's Pharmacy. I would like just the logo on one side, maybe with black background and white lettering. The other side I would also like to include my logo which is attached. Also, please include my name and the following information:
Rolf Mayhew Owner/Pharm D.
Business address is 7314 N Birchwood Rd Alder Bluff, NV 57193.
Phone number is 555-318-2067 and fax # is 555-318-2063.
my email address is kip@kipsrxhall.com.
My website is www.kipsrxhall.com.
My business hours are Monday-Friday 8am-7 pm. Saturday 8am-12 pm. Sunday Closed.
I would like the design to include my logo colors, black, white, and neon green. Silver may be added as a highlight. Thanks.
Industry/Entity Type
Pharmacy
Contact Information for Business Card
See above in product description
Look and feel

```html
<!DOCTYPE html>
<html lang="en">
<head>
<meta charset="utf-8">
<title>Kip's Pharmacy – Business Card</title>
<link rel="stylesheet" href="https://fonts.googleapis.com/css2?family=Open+Sans:wght@400;600;700&display=swap">
<style>
  :root {
    --backdrop: #b9b9b9;
    --card: #262424;
    --ink: #ffffff;
    --ink-soft: #e6e6e6;
    --neon: #8cc63f;
    --silver: #9a9a9a;
  }
  * { box-sizing: border-box; margin: 0; padding: 0; }
  html, body {
    width: 1200px; height: 900px; overflow: hidden;
    background: var(--backdrop);
    font-family: "Open Sans", Arial, sans-serif;
    color: var(--ink);
  }
  .canvas { position: relative; width: 1200px; height: 900px; }

  .card {
    position: absolute;
    width: 560px; height: 320px;
    background: var(--card);
    box-shadow: 0 6px 18px rgba(0,0,0,.35);
  }
  .card--back { left: 590px; top: 110px; }
  .card--front { left: 50px; top: 470px; }

  /* Logo lockup */
  .lockup { position: absolute; display: flex; align-items: center; }
  .lockup__dot { width: 34px; height: 34px; border-radius: 50%; background: var(--neon); flex: none; }
  .lockup__rule { width: 1px; height: 62px; background: var(--silver); margin: 0 20px; }
  .lockup__name { font-weight: 600; font-size: 38px; letter-spacing: -0.5px; color: var(--ink); white-space: nowrap; }

  .card--back .lockup { left: 0; right: 0; top: 128px; justify-content: center; }
  .card--front .lockup { left: 150px; top: 34px; }
  .card--front .lockup__name { font-size: 32px; }

  /* Person */
  .person { position: absolute; left: 0; right: 0; top: 120px; text-align: center; }
  .person__name { font-weight: 700; font-size: 22px; letter-spacing: 3px; }
  .person__title { font-size: 13px; letter-spacing: 1px; color: var(--ink-soft); margin-top: 2px; }

  /* Contact row */
  .contacts {
    position: absolute; left: 24px; right: 24px; bottom: 34px;
    display: flex; align-items: center; justify-content: space-between;
    font-size: 12.5px; color: var(--ink-soft);
  }
  .contacts__group { display: flex; flex-direction: column; gap: 5px; }
  .contacts__line { display: flex; align-items: flex-start; gap: 7px; line-height: 1.35; white-space: nowrap; }
  .contacts__icon { width: 12px; height: 12px; flex: none; margin-top: 2px; fill: var(--ink); }
  .contacts__divider {
    width: 1px; height: 56px;
    background: linear-gradient(to bottom, transparent, var(--neon), transparent);
  }
</style>
</head>
<body>
<main class="canvas">

  <section class="card card--back" aria-label="Card back">
    <div class="lockup">
      <span class="lockup__dot"></span>
      <span class="lockup__rule"></span>
      <span class="lockup__name">Kip's Pharmacy</span>
    </div>
  </section>

  <section class="card card--front" aria-label="Card front">
    <div class="lockup">
      <span class="lockup__dot"></span>
      <span class="lockup__rule"></span>
      <span class="lockup__name">Kip's Pharmacy</span>
    </div>

    <div class="person">
      <p class="person__name">Rolf Mayhew</p>
      <p class="person__title">Owner/Pharm D.</p>
    </div>

    <div class="contacts">
      <div class="contacts__group">
        <p class="contacts__line">
          <svg class="contacts__icon" viewBox="0 0 12 12"><path d="M0 2h12v8H0z M1 3v.4l5 3.2 5-3.2V3z" fill-rule="evenodd"/></svg>
          kip@kipsrxhall.com
        </p>
        <p class="contacts__line">
          <svg class="contacts__icon" viewBox="0 0 12 12"><circle cx="6" cy="6" r="5.5" fill="none" stroke="#fff"/><ellipse cx="6" cy="6" rx="2.2" ry="5.5" fill="none" stroke="#fff" stroke-width=".8"/><path d="M.5 6h11" stroke="#fff" stroke-width=".8"/></svg>
          www.kipsrxhall.com
        </p>
      </div>

      <span class="contacts__divider"></span>

      <div class="contacts__group">
        <p class="contacts__line">
          <svg class="contacts__icon" viewBox="0 0 12 12"><path d="M2.5 0.5l2 2.6-1.2 1.4c.8 1.7 2.2 3.1 3.9 3.9l1.4-1.2 2.6 2-1.5 2.3C5 11.2.8 7 .3 2z"/></svg>
          555-318-2067
        </p>
        <p class="contacts__line">
          <svg class="contacts__icon" viewBox="0 0 12 12"><path d="M3 0h6v3H3z M1 4h10v6H1z M3 8h6v4H3z" fill-rule="evenodd"/></svg>
          555-318-2063
        </p>
      </div>

      <span class="contacts__divider"></span>

      <div class="contacts__group">
        <p class="contacts__line">
          <svg class="contacts__icon" viewBox="0 0 12 12"><path d="M6 0a4 4 0 0 1 4 4c0 3-4 8-4 8S2 7 2 4a4 4 0 0 1 4-4zm0 2.4a1.6 1.6 0 1 0 0 3.2 1.6 1.6 0 0 0 0-3.2z" fill-rule="evenodd"/></svg>
          <span>7314 N Birchwood Rd,<br>Alder Bluff, NV 57193</span>
        </p>
      </div>
    </div>
  </section>

</main>
</body>
</html>
```